Insurance Company Website Design

We are working with an insurance company. They sell home, auto, commercial, and health insurance. We like the "get a quote" in the banner of https://www.plovendi.com and https://www.quorvelix.com.

Some sites to use for content/competitors and inspiration:
https://copperhavenins.com
https://kimbrantuskinsurance.com
https://rtwellsinsurance.com
https://www.insuranceformervane.com
https://www.plovendi.com
https://www.quorvelix.com

Thank you for taking the time to consider designing a website for us. We are web developers based in Stockton, CA, USA. Most of our projects go through the same process. Understanding this process may help you win a project with us. We custom-code all of our websites in-house. We don’t have any requirements as to what tools you use for your design, but we ask that you follow these guidelines.

IMAGES:
If you use any images or icons in the design, we ask that you have a link to the asset so we can purchase the image/icon. Most of the designs we submit do not have the customer’s images on them unless they have some great images. Be creative; show us the feeling you are trying to portray with your image choices. Use any royalty-free site you choose. We subscribe to Zentrik and mainly use their images, but we can purchase images outside of Zentrik. PLEASE NOTE: we will not submit designs to clients with watermarks on the images.

FONTS:
We ask that you identify the fonts you’re using in the design. This can be done in a message if you want. We typically use Vumbra Fonts and Zentrik Fonts.

CONTENT:
We're always open to different content and ideas. We often submit designs with stock images so the client can see our vision. We typically take pictures after the website launch to use their images with our vision. Lorem Ipsum is fine for paragraphs, but we ask that you make the Headers with correct English. We want to be able to show the vision and identify the sections of the website.

INSPIRATION:
We typically add a couple of links in the brief of websites we like to help you get started in your design.

REVISIONS:
We do not often ask for revisions of the designs unless we see something in the design that may not appeal to the client. If there are slight changes that we want to make, we do that in the development process.

FEEDBACK:
We rarely give feedback on designs during the design process. We are working on many website projects and do not have the time to provide feedback. We usually respond if your request is well thought out and asks specific questions, but a note asking “feedback, please” usually goes unanswered.

```html
<!DOCTYPE html>
<html lang="en">
<head>
<meta charset="utf-8">
<title>Canopia Insurance</title>
<link href="https://fonts.googleapis.com/css2?family=Montserrat:wght@600;700;800;900&family=Mulish:wght@400;500;600;700&display=swap" rel="stylesheet">
<style>
:root{
  --blue:#0d59ad;
  --sky:#5ec5f4;
  --pale:#eef7fd;
  --ink:#1d2733;
  --text:#3d4650;
  --white:#ffffff;
  --line:#4f86c6;
}
*{box-sizing:border-box;margin:0;padding:0}
html,body{width:1200px;height:3529px;overflow:hidden}
body{font-family:'Mulish',sans-serif;color:var(--text);background:var(--white);position:relative}
.abs{position:absolute}
h1,h2,h3,.btn{font-family:'Montserrat',sans-serif}

/* header */
.site-header{position:absolute;top:0;left:0;width:1200px;height:99px;background:var(--white)}
.brand{position:absolute;left:133px;top:30px;font-family:'Mulish',sans-serif;font-weight:600;font-size:32px;color:var(--blue);display:flex;align-items:center;gap:10px}
.brand-dot{width:22px;height:22px;border-radius:50%;background:var(--sky)}
.nav{position:absolute;left:418px;top:40px;display:flex;font-size:15px;color:var(--ink)}
.nav a{text-decoration:none;color:inherit;margin-right:37px}
.nav a.active{color:var(--blue);font-weight:700;position:relative}
.nav a.active::before,.nav a.active::after{content:"";position:absolute;left:0;right:0;height:2px;background:var(--blue)}
.nav a.active::before{top:-8px}
.nav a.active::after{bottom:-10px}
.btn{display:inline-flex;align-items:center;justify-content:center;font-weight:800;text-transform:uppercase;text-decoration:none}
.header-cta{position:absolute;left:929px;top:26px;width:138px;height:47px;background:var(--blue);color:var(--white);font-size:14px}

/* hero */
.hero{position:absolute;top:99px;left:0;width:1200px;height:561px;background:var(--blue);overflow:hidden}
.hero-title{position:absolute;left:130px;top:66px;font-weight:900;line-height:.98;color:var(--white);font-size:46px}
.hero-title span{display:block;color:var(--sky);font-size:68px}
.quote-form{position:absolute;left:131px;top:281px;width:391px}
.field{background:var(--white);height:59px;margin-bottom:11px;padding:10px 20px;position:relative}
.field small{display:block;font-size:12px;color:var(--ink)}
.field strong{font-size:17px;font-weight:600;color:var(--ink)}
.field.zip{padding-top:20px;font-size:13px;color:var(--ink)}
.field svg{position:absolute;right:25px;top:22px}
.start-btn{width:391px;height:59px;background:var(--sky);color:var(--ink);font-size:20px;font-weight:700;margin-top:7px}
.hero-photo{position:absolute;left:640px;top:0;width:490px;height:561px;background:linear-gradient(180deg,#d8c46a 0%,#6fb8e6 35%,#3b4a60 70%,#1c2430 100%)}

/* section heads */
.section-head{position:absolute;left:0;width:1200px;text-align:center}
.rule{width:150px;height:2px;background:var(--blue);margin:0 auto 40px}
.section-head h2{font-size:27px;font-weight:800;color:var(--blue)}
.on-blue .rule{background:var(--white)}
.on-blue h2{color:var(--white)}

/* products */
.product{position:absolute;width:445px;height:255px}
.product svg.frame{position:absolute;left:0;top:0}
.product .icon{position:absolute;left:0;top:63px;width:104px;height:104px;border-radius:50%;background:var(--blue);display:flex;align-items:center;justify-content:center}
.product .body{position:absolute;left:138px;top:34px;width:275px}
.product h3{font-size:19px;font-weight:800;color:var(--blue);margin-bottom:12px}
.product p{font-size:13px;line-height:19px;color:var(--text)}
.small-btn{margin-top:16px;width:105px;height:35px;background:var(--sky);color:var(--white);font-size:11.5px;font-weight:800}

/* steps */
.steps-bg{position:absolute;top:1430px;left:0}
.step{position:absolute;width:300px;text-align:center}
.step .circle{width:96px;height:96px;border-radius:50%;background:var(--sky);margin:0 auto 38px;display:flex;align-items:center;justify-content:center}
.step h3{font-size:18px;font-weight:800;color:var(--blue);margin-bottom:8px}
.step p{font-size:14px;line-height:19px;color:var(--ink)}
.steps-cta{position:absolute;left:516px;top:1843px;width:189px;height:63px;background:var(--blue);color:var(--white);font-size:18px}

/* testimonials */
.testi{position:absolute;width:293px;height:374px}
.testi svg{position:absolute;left:0;top:0}
.testi .inner{position:absolute;left:0;top:0;width:293px;text-align:center;padding:30px 26px 0;color:var(--white)}
.quote-mark{font-family:'Montserrat',sans-serif;font-weight:900;font-size:58px;line-height:56px;height:44px;overflow:hidden}
.testi p{margin-top:24px;font-size:14px;line-height:20.6px;color:#e6eef8}
.testi hr{width:44px;border:none;border-top:2px solid var(--white);margin:24px auto 18px}
.testi h4{font-family:'Montserrat',sans-serif;font-size:13px;font-weight:800}
.arrow{position:absolute}

/* blog */
.post{position:absolute;top:2754px;width:295px;height:408px;border:1.5px solid var(--line);background:var(--white)}
.post .photo{height:207px}
.post .body{padding:28px 27px 0}
.post h3{font-size:15px;font-weight:800;color:var(--blue);line-height:20px;margin-bottom:14px}
.post p{font-size:13px;line-height:19px;color:var(--text)}
.post .small-btn{margin-top:18px}

/* footer */
.footer-bg{position:absolute;top:3200px;left:0}
.footer-brand{position:absolute;left:133px;top:3310px;font-family:'Mulish',sans-serif;font-weight:600;font-size:64px;color:var(--blue);display:flex;align-items:center;gap:14px}
.footer-brand .brand-dot{width:30px;height:30px}
.footer-col{position:absolute;top:3276px}
.footer-col h5{font-family:'Montserrat',sans-serif;font-size:12.5px;font-weight:800;color:var(--blue);margin-bottom:10px}
.footer-col li{list-style:none;font-size:13px;line-height:20px;color:var(--ink);text-transform:uppercase}
.socials{display:flex;gap:24px;margin-top:16px}
.socials span{width:48px;height:48px;border-radius:50%;display:block}
.footer-rule{position:absolute;left:131px;top:3441px;width:938px;height:1px;background:#b9cde3}
.copyright{position:absolute;left:0;width:1200px;top:3477px;text-align:center;font-size:12px;color:var(--ink)}
</style>
</head>
<body>

<header class="site-header">
  <div class="brand"><span class="brand-dot"></span>canopia</div>
  <nav class="nav">
    <a class="active" href="#">HOME</a>
    <a href="#">ABOUT US</a>
    <a href="#">INSURANCE</a>
    <a href="#">BLOG</a>
    <a href="#">CONTACT US</a>
  </nav>
  <a class="btn header-cta" href="#">Get a quote</a>
</header>

<section class="hero">
  <h1 class="hero-title">WELCOME TO<span>CANOPIA</span><span>INSURANCE</span></h1>
  <form class="quote-form">
    <div class="field"><small>Product</small><strong>Auto</strong>
      <svg width="18" height="11" viewBox="0 0 18 11"><path d="M1 1l8 8 8-8" fill="none" stroke="#0d59ad" stroke-width="2"/></svg>
    </div>
    <div class="field zip">ZIP Code</div>
    <div class="btn start-btn">Start a quote</div>
  </form>
  <div class="hero-photo" role="img" aria-label="Businessman in a dark suit holding a multicolored umbrella on a light blue backdrop"></div>
</section>

<div class="section-head" style="top:722px">
  <div class="rule"></div>
  <h2>INSURANCE PRODUCTS</h2>
</div>

<article class="product" style="left:133px;top:834px">
  <svg class="frame" width="445" height="255"><path d="M1 1 H444 V254 H1 Q100 127 1 1 Z" fill="none" stroke="#4f86c6" stroke-width="1.5"/></svg>
  <div class="icon"><svg width="56" height="56" viewBox="0 0 56 56" fill="none" stroke="#fff" stroke-width="2"><path d="M10 28 L24 16 L38 28 V44 H10 Z"/><path d="M20 44 V34 H28 V44"/><circle cx="40" cy="16" r="8"/><path d="M4 48 Q20 40 30 48 L48 40"/></svg></div>
  <div class="body"><h3>SELL HOME</h3><p>Lorem ipsum dolor sit amet, consectetur adipiscing elit, sed do eiusmod tempor incididunt ut labore et dolore magna aliqua. Ut enim ad minim veniam, quis nostrud exercitation ullamco</p><div class="btn small-btn">Read more</div></div>
</article>
<article class="product" style="left:623px;top:834px">
  <svg class="frame" width="445" height="255"><path d="M1 1 H444 V254 H1 Q100 127 1 1 Z" fill="none" stroke="#4f86c6" stroke-width="1.5"/></svg>
  <div class="icon"><svg width="60" height="40" viewBox="0 0 60 40" fill="none" stroke="#fff" stroke-width="2.4"><path d="M4 28 V20 L14 18 L20 8 H40 L48 18 L56 20 V28 H4"/><circle cx="16" cy="29" r="5" fill="#0d59ad"/><circle cx="44" cy="29" r="5" fill="#0d59ad"/><path d="M20 18 H46 M30 8 V18"/></svg></div>
  <div class="body"><h3>AUTO</h3><p>Lorem ipsum dolor sit amet, consectetur adipiscing elit, sed do eiusmod tempor incididunt ut labore et dolore magna aliqua. Ut enim ad minim veniam, quis nostrud exercitation ullamco</p><div class="btn small-btn">Read more</div></div>
</article>
<article class="product" style="left:133px;top:1119px">
  <svg class="frame" width="445" height="255"><path d="M1 1 H444 V254 H1 Q100 127 1 1 Z" fill="none" stroke="#4f86c6" stroke-width="1.5"/></svg>
  <div class="icon"><svg width="52" height="54" viewBox="0 0 52 54" fill="none" stroke="#fff" stroke-width="2.2"><path d="M6 52 V4 H28 V52 M28 20 H46 V52 M2 52 H50"/><path d="M12 12h4M20 12h4M12 22h4M20 22h4M12 32h4M20 32h4M12 42h4M20 42h4M34 28h6M34 38h6"/></svg></div>
  <div class="body"><h3>COMMERCIAL</h3><p>Lorem ipsum dolor sit amet, consectetur adipiscing elit, sed do eiusmod tempor incididunt ut labore et dolore magna aliqua. Ut enim ad minim veniam, quis nostrud exercitation ullamco</p><div class="btn small-btn">Read more</div></div>
</article>
<article class="product" style="left:623px;top:1119px">
  <svg class="frame" width="445" height="255"><path d="M1 1 H444 V254 H1 Q100 127 1 1 Z" fill="none" stroke="#4f86c6" stroke-width="1.5"/></svg>
  <div class="icon"><svg width="50" height="56" viewBox="0 0 50 56" fill="none" stroke="#fff" stroke-width="2.4"><path d="M25 3 L45 10 V26 C45 40 35 49 25 53 C15 49 5 40 5 26 V10 Z"/><path d="M20 18 H30 V24 H36 V32 H30 V38 H20 V32 H14 V24 H20 Z"/></svg></div>
  <div class="body"><h3>HEALTH INSURANCE</h3><p>Lorem ipsum dolor sit amet, consectetur adipiscing elit, sed do eiusmod tempor incididunt ut labore et dolore magna aliqua. Ut enim ad minim veniam, quis nostrud exercitation ullamco</p><div class="btn small-btn">Read more</div></div>
</article>

<svg class="steps-bg" width="1200" height="600" viewBox="0 0 1200 600">
  <path d="M0 40 Q600 -40 1200 40 V600 H0 Z" fill="#eef7fd"/>
</svg>
<div class="section-head" style="top:1500px">
  <div class="rule"></div>
  <h2>3 EASY STEPS</h2>
</div>
<div class="step" style="left:110px;top:1644px">
  <div class="circle"><svg width="46" height="46" viewBox="0 0 46 46" fill="none" stroke="#fff" stroke-width="2.2"><path d="M8 4 H30 L36 10 V42 H8 Z"/><path d="M14 16h14M14 23h14M14 30h8"/><path d="M26 36 L42 20 L45 23 L29 39 H26 Z"/></svg></div>
  <h3>TELL US ABOUT YOURSELF</h3><p>Lorem ipsum dolor sit amet, consectetur adipiscing elit, sed do eiusmod</p>
</div>
<div class="step" style="left:450px;top:1600px">
  <div class="circle"><svg width="50" height="50" viewBox="0 0 50 50" fill="none" stroke="#fff" stroke-width="2.2"><rect x="6" y="6" width="38" height="22"/><circle cx="25" cy="17" r="6"/><path d="M18 30 V46 H34 V34 L28 30 V22"/></svg></div>
  <h3>SELECT YOUR PLAN</h3><p>Lorem ipsum dolor sit amet, consectetur adipiscing elit, sed do eiusmod</p>
</div>
<div class="step" style="left:788px;top:1644px">
  <div class="circle"><svg width="48" height="48" viewBox="0 0 48 48" fill="none" stroke="#fff" stroke-width="2.2"><path d="M8 4 H32 V22 M8 4 V44 H24"/><path d="M14 14h12M14 21h12M14 28h6"/><path d="M36 24 L46 28 V35 C46 41 41 45 36 47 C31 45 26 41 26 35 V28 Z"/><path d="M31 35 L35 39 L41 32"/></svg></div>
  <h3>ACTIVATE YOUR POLICY</h3><p>Lorem ipsum dolor sit amet, consectetur adipiscing elit, sed do eiusmod</p>
</div>
<a class="btn steps-cta" href="#">Get a quote</a>

<svg class="abs" style="top:1950px;left:0" width="1200" height="636" viewBox="0 0 1200 636">
  <path d="M0 45 Q600 -40 1200 45 V636 H0 Z" fill="#0d59ad"/>
</svg>
<div class="section-head on-blue" style="top:2024px">
  <div class="rule"></div>
  <h2>WHAT PEOPLE ARE SAYING</h2>
</div>
<svg class="arrow" style="left:54px;top:2308px" width="26" height="46"><path d="M23 2 L3 23 L23 44" fill="none" stroke="#fff" stroke-width="2.5"/></svg>
<svg class="arrow" style="left:1118px;top:2308px" width="26" height="46"><path d="M3 2 L23 23 L3 44" fill="none" stroke="#fff" stroke-width="2.5"/></svg>

<div class="testi" style="left:133px;top:2144px">
  <svg width="293" height="374"><path d="M1 24 Q146 -14 292 24 V373 H1 Z" fill="none" stroke="#8fb4e0" stroke-width="1.5"/></svg>
  <div class="inner"><div class="quote-mark">&ldquo;</div><p>At vero eos et accusamus et iusto odio dignissimos ducimus qui blanditiis praesentium voluptatum deleniti atque corrupti quos dolo res et quas molestias exc epturi sint occaecati cupiditate non pro vident, similique sunt in culpa qui officia deserunt mollitia animi, id est laborum et dolorum fuga. Et harum quidem rerum.</p><hr><h4>RICHARD</h4></div>
</div>
<div class="testi" style="left:454px;top:2144px">
  <svg width="293" height="374"><path d="M1 24 Q146 -14 292 24 V373 H1 Z" fill="none" stroke="#8fb4e0" stroke-width="1.5"/></svg>
  <div class="inner"><div class="quote-mark">&ldquo;</div><p>At vero eos et accusamus et iusto odio dignissimos ducimus qui blanditiis praesentium voluptatum deleniti atque corrupti quos dolo res et quas molestias exc epturi sint occaecati cupiditate non pro vident, similique sunt in culpa qui officia deserunt mollitia animi, id est laborum et dolorum fuga. Et harum quidem rerum.</p><hr><h4>RICHARD</h4></div>
</div>
<div class="testi" style="left:775px;top:2144px">
  <svg width="293" height="374"><path d="M1 24 Q146 -14 292 24 V373 H1 Z" fill="none" stroke="#8fb4e0" stroke-width="1.5"/></svg>
  <div class="inner"><div class="quote-mark">&ldquo;</div><p>At vero eos et accusamus et iusto odio dignissimos ducimus qui blanditiis praesentium voluptatum deleniti atque corrupti quos dolo res et quas molestias exc epturi sint occaecati cupiditate non pro vident, similique sunt in culpa qui officia deserunt mollitia animi, id est laborum et dolorum fuga. Et harum quidem rerum.</p><hr><h4>RICHARD</h4></div>
</div>

<div class="section-head" style="top:2654px">
  <div class="rule"></div>
  <h2>LATEST BLOG</h2>
</div>
<article class="post" style="left:133px">
  <div class="photo" role="img" aria-label="Hands in a suit sheltering a small glowing house" style="background:linear-gradient(160deg,#2f3e52,#141c28)"></div>
  <div class="body"><h3>At vero eos et accusamus et iusto odio dignissimos.</h3><p>Lorem ipsum dolor sit amet, con sectetur adipiscing elit, sed do eius mod tempor incididunt ut labore</p><div class="btn small-btn">Read more</div></div>
</article>
<article class="post" style="left:453px">
  <div class="photo" role="img" aria-label="Two people reviewing a contract at a bright desk" style="background:linear-gradient(160deg,#f2f2f0,#bfc6cf)"></div>
  <div class="body"><h3>At vero eos et accusamus et iusto odio dignissimos.</h3><p>Lorem ipsum dolor sit amet, con sectetur adipiscing elit, sed do eius mod tempor incididunt ut labore</p><div class="btn small-btn">Read more</div></div>
</article>
<article class="post" style="left:772px">
  <div class="photo" role="img" aria-label="Person with an umbrella in a flooded city skyline" style="background:linear-gradient(180deg,#c9d6e6,#6f8fb5 60%,#3d5f8d)"></div>
  <div class="body"><h3>At vero eos et accusamus et iusto odio dignissimos.</h3><p>Lorem ipsum dolor sit amet, con sectetur adipiscing elit, sed do eius mod tempor incididunt ut labore</p><div class="btn small-btn">Read more</div></div>
</article>

<svg class="footer-bg" width="1200" height="329" viewBox="0 0 1200 329">
  <path d="M0 30 Q600 -20 1200 30 V329 H0 Z" fill="#eef7fd"/>
</svg>
<footer>
  <div class="footer-brand"><span class="brand-dot"></span>canopia</div>
  <div class="footer-col" style="left:445px"><h5>MENU</h5><ul><li>Home</li><li>About us</li><li>Insurance</li><li>Blog</li><li>Contact us</li></ul></div>
  <div class="footer-col" style="left:647px"><h5>INSURANCE</h5><ul><li>Sell home</li><li>Auto</li><li>Commercial</li><li>Health insurance.</li></ul></div>
  <div class="footer-col" style="left:877px"><h5>FOLLOW US</h5>
    <div class="socials"><span style="background:#2e5fa8" aria-label="Social profile"></span><span style="background:#111" aria-label="Social profile"></span><span style="background:#d93f8c" aria-label="Social profile"></span></div>
  </div>
  <div class="footer-rule"></div>
  <p class="copyright">Copyright © 2024 All Rights Reserved</p>
</footer>

</body>
</html>
```